Biodegradable box for eco-friendly bamboo cotton buds

I am looking for a design on a box holding 200 bamboo cotton buds. The box opens like a matchstick box and is made from recycled card. It's to sell online and at markets, maybe also supermarkets.
It's the second product my company, LeafMarta, will sell, so I would like a design that I can replicate on other product packaging in the future.
You can see more about LeafMarta on my website www.leafmarta.org or facebook and instagram @leafmartaqatar.
Please see below the box dimensions from the supplier and a photo. Also, some ideas I have had using Canva. I would like to see the green strip go all the way round the box. I like the font. The cotton bud logo is copyrighted - I like the style, but a new one would need to be created.

Target Market(s)

Eco-conscious consumers - expats and locals - in Qatar

Industry/Entity Type

Retail

Font styles to use
Other font styles liked:
• special elite

Colors
cadf82
acd037
eaf2ce
9ccb3b

Requirements
Must have
• an environmentally-friendly focus

```html
<!DOCTYPE html>
<html lang="en">
<head>
<meta charset="utf-8">
<title>LeafMarta Bamboo Cotton Buds – Box Panels</title>
<link href="https://fonts.googleapis.com/css2?family=Special+Elite&family=Fredoka:wght@500&family=Montserrat:wght@300&display=swap" rel="stylesheet">
<style>
  :root{
    --kraft:#d8cbb2;
    --green:#8fb83a;
    --green-text:#8cb43c;
    --green-soft:#cadf82;
    --pale:#eaf2ce;
    --ink:#7fa832;
    --white:#ffffff;
    --bg-a:#f6f6f6;
    --bg-b:#dedede;
  }
  *{box-sizing:border-box;margin:0;padding:0}
  html,body{width:1200px;height:1200px;overflow:hidden}
  body{
    background:radial-gradient(circle at 50% 45%,var(--bg-a) 0%,var(--bg-b) 100%);
    position:relative;
    font-family:"Special Elite",monospace;
  }
  .panel{
    position:absolute;left:140px;width:920px;height:500px;
    background:var(--kraft);
    overflow:hidden;
    box-shadow:0 6px 18px rgba(0,0,0,.12);
  }
  .panel--back{top:60px}
  .panel--front{top:640px}
  .band{position:absolute;inset:0;width:920px;height:500px}
  .band path{fill:var(--green)}

  .brand{
    position:absolute;color:var(--white);
    font-family:"Montserrat",sans-serif;font-weight:300;font-size:30px;
    display:flex;align-items:center;gap:10px;letter-spacing:.5px;
  }
  .brand__dot{width:14px;height:14px;border-radius:50%;background:var(--white)}
  .brand--flipped{transform:rotate(180deg)}

  /* back panel */
  .eco-badge{
    position:absolute;left:70px;top:40px;width:110px;height:110px;border-radius:50%;
    border:4px solid var(--green-text);
  }
  .care-copy{
    position:absolute;left:200px;top:50px;width:340px;
    color:var(--green-text);font-size:15px;line-height:1.35;text-align:center;
  }
  .care-copy p{margin-bottom:12px}
  .care-copy .warning{font-weight:bold;font-size:17px;color:var(--ink);margin-bottom:0}
  .origin{
    position:absolute;left:380px;top:312px;display:flex;align-items:center;gap:12px;
    font-family:"Montserrat",sans-serif;font-size:14px;color:var(--green-text);
  }
  .origin__mark{width:30px;height:22px;border:2px solid var(--green-text)}
  .side-strip{
    position:absolute;left:0;right:0;top:360px;height:2px;background:rgba(140,180,60,.35);
  }
  .find-more{
    position:absolute;left:200px;top:385px;width:320px;
    transform:rotate(180deg);color:var(--green-text);font-size:15px;text-align:center;line-height:1.4;
  }
  .find-more .handle{display:flex;justify-content:center;align-items:center;gap:8px}
  .find-more .handle span.sq{width:14px;height:14px;border:2px solid var(--green-text)}

  /* front panel */
  .hero-art{
    position:absolute;left:150px;top:30px;width:330px;height:140px;border-radius:14px;
    background:linear-gradient(135deg,var(--pale),var(--green-soft));
  }
  .title{
    position:absolute;left:100px;top:178px;width:430px;
    font-family:"Fredoka",sans-serif;font-weight:500;color:var(--green-soft);
    font-size:56px;line-height:.95;text-align:center;letter-spacing:1px;
  }
  .count{
    position:absolute;left:370px;top:292px;font-size:18px;color:var(--green-text);
  }
  .claims{position:absolute;left:120px;top:325px;width:400px;color:var(--green-text)}
  .claim{display:flex;align-items:center;justify-content:flex-end;gap:16px;padding:5px 0}
  .claim + .claim{border-top:2px solid var(--green-text)}
  .claim__text{text-align:right;font-size:13px;line-height:1.1}
  .claim__text b{display:block;font-size:22px;font-weight:normal}
  .claim__icon{width:42px;height:38px;border-radius:50%;background:var(--green-text)}
  .claim__icon--box{border-radius:6px}
</style>
</head>
<body>

<section class="panel panel--back" aria-label="Box back panel">
  <svg class="band" viewBox="0 0 920 500" aria-hidden="true">
    <path d="M580,0 l-18,12.5 l18,12.5 l-18,12.5 l18,12.5 l-18,12.5 l18,12.5 l-18,12.5 l18,12.5 l-18,12.5 l18,12.5 l-18,12.5 l18,12.5 l-18,12.5 l18,12.5 l-18,12.5 l18,12.5 l-18,12.5 l18,12.5 l-18,12.5 l18,12.5 l-18,12.5 l18,12.5 l-18,12.5 l18,12.5 l-18,12.5 l18,12.5 l-18,12.5 l18,12.5 l-18,12.5 l18,12.5 l-18,12.5 l18,12.5 l-18,12.5 l18,12.5 l-18,12.5 l18,12.5 l-18,12.5 l18,12.5 l-18,12.5 l18,12.5 H880 V0 Z"/>
  </svg>

  <div class="eco-badge" role="img" aria-label="Eco friendly stamp"></div>

  <div class="care-copy">
    <p>Cotton buds have many uses, cleaning your ears is not one of them!</p>
    <p>Ear wax is your ear's natural way of cleaning itself. Putting buds in disrupts this process and damages the ear canal.</p>
    <p class="warning">Never put anything smaller than your elbow in your ear!</p>
  </div>

  <div class="origin"><span>Made in China</span><span class="origin__mark" role="img" aria-label="Conformity mark"></span></div>

  <div class="brand" style="left:640px;top:250px"><span class="brand__dot"></span>LeafMarta</div>

  <div class="side-strip" aria-hidden="true"></div>

  <div class="find-more">
    <p>Find more products<br>at www.leafmarta.org</p>
    <p class="handle"><span class="sq"></span><span class="sq"></span>@leafmartaqatar</p>
  </div>

  <div class="brand brand--flipped" style="left:640px;top:405px"><span class="brand__dot"></span>LeafMarta</div>
</section>

<section class="panel panel--front" aria-label="Box front panel">
  <svg class="band" viewBox="0 0 920 500" aria-hidden="true">
    <path d="M580,0 l-18,12.5 l18,12.5 l-18,12.5 l18,12.5 l-18,12.5 l18,12.5 l-18,12.5 l18,12.5 l-18,12.5 l18,12.5 l-18,12.5 l18,12.5 l-18,12.5 l18,12.5 l-18,12.5 l18,12.5 l-18,12.5 l18,12.5 l-18,12.5 l18,12.5 l-18,12.5 l18,12.5 l-18,12.5 l18,12.5 l-18,12.5 l18,12.5 l-18,12.5 l18,12.5 l-18,12.5 l18,12.5 l-18,12.5 l18,12.5 l-18,12.5 l18,12.5 l-18,12.5 l18,12.5 l-18,12.5 l18,12.5 l-18,12.5 l18,12.5 H880 V0 Z"/>
  </svg>

  <div class="hero-art" role="img" aria-label="Illustration of crossed bamboo cotton buds with bamboo leaves and a cotton boll"></div>

  <h1 class="title">bamboo<br>cotton buds</h1>
  <p class="count">200 Buds</p>

  <div class="claims">
    <div class="claim">
      <div class="claim__text"><b>100%</b>biodegradable<br>buds</div>
      <span class="claim__icon" role="img" aria-label="Leaf and recycling icon"></span>
    </div>
    <div class="claim">
      <div class="claim__text"><b>100%</b>biodegradable<br>packaging</div>
      <span class="claim__icon claim__icon--box" role="img" aria-label="Recyclable box icon"></span>
    </div>
  </div>

  <div class="brand" style="left:640px;top:150px"><span class="brand__dot"></span>LeafMarta</div>
  <div class="brand" style="left:640px;top:400px"><span class="brand__dot"></span>LeafMarta</div>
</section>

</body>
</html>
```